trailbuzz.example - youth/backpackers Adventure Travel contact site

Landing Page: Logo, @RoamQuestOutfitters, Australia | New Zealand | Fiji | South East Asia, Start Button, a Rotating carousel of supplier logos, ©Trail Buzz Journeys, Terms and Conditions link, Contact Us page link, social media/contact icons.
Start Button: Takes you to destinations selection Map - Hover over effect with selectable Countries, states, regions, and next & back buttons.
Next Button: Takes you to Activities - Selectable Buttons for Sky Diving, Sailing, Whitewater Rafting, Bungee jumping, camping, hiking, Surfing, Jet Boating, kayaking, canyoning, National Parks, Scuba Diving, Snorkeling and beaches etc., Tandem Hand gliding, with a typable "Have we missed anything you want to experience" area and back and next buttons.
Next Button: Takes you to extras - Selectable buttons for Bus Passes, Accommodation, Car Hire, Camper Hire and back and next buttons.
Next Button: Takes you to enter customer details: Name, Age, Phone, Email, How did you hear about us, Dietary requirement, start & end date, start & end location, Number of Travellers, Budget, anything else area, Submit for your custom adventure button. - All this information then gets emailed.

Target Market(s)

Backpacker/youth adventure travel

Industry/Entity Type

Travel Agent

Coding

Coded - Design and coding required

Number of Pages Required

3 page

Colors

Designer to choose colors to be used in the design.

Requirements
Must have
• Somewhere to be automatically synced Instagram profile pictures and videos.
• Full screen, scalable to any device size - 65% of our users use mobile devices.
• Wordpress
Nice to have
• Easy to add and remove selectable buttons
• If you can think of any special feature to add ;)
Should not have
• Basic contact form look

```html
<!DOCTYPE html>
<html lang="en">
<head>
<meta charset="utf-8">
<title>Trail Buzz Journeys – Adventure Travel</title>
<link href="https://fonts.googleapis.com/css2?family=Open+Sans:wght@400;600;700&display=swap" rel="stylesheet">
<style>
  :root {
    --coral: #f05543;
    --navy: #2e3a55;
    --ink: #222a3a;
    --panel: rgba(255, 255, 255, 0.88);
    --band: #f2f2f2;
    --brand-grey: #5a5a5a;
    --arrow-grey: #a9a9a9;
    --white: #ffffff;
    --sky-top: #a9c3dc;
    --sky-mid: #d6e2ec;
    --ridge: #8ea6bd;
    --ridge-deep: #6f8aa4;
    --social-1: #3b5998;
    --social-2: #1da1f2;
    --social-3: #e24a33;
    --social-4: #c8232c;
    --social-5: #f57d00;
    --social-6: #e52d27;
    --social-7: #517fa4;
  }
  * { box-sizing: border-box; margin: 0; padding: 0; }
  html, body { width: 1200px; height: 614px; overflow: hidden; }
  body { font-family: 'Open Sans', Arial, sans-serif; background: var(--white); color: var(--ink); position: relative; }

  .hero { position: absolute; left: 0; top: 0; width: 1200px; height: 448px; overflow: hidden; }
  .hero-scene {
    position: absolute; inset: 0;
    background:
      linear-gradient(180deg, transparent 55%, rgba(111,138,164,0.55) 100%),
      linear-gradient(180deg, var(--sky-top) 0%, var(--sky-mid) 45%, var(--ridge) 80%, var(--ridge-deep) 100%);
  }

  .brand {
    position: absolute; left: 132px; top: 66px;
    display: flex; align-items: center; gap: 10px;
  }
  .brand-dot { width: 34px; height: 34px; border-radius: 50%; background: var(--coral); }
  .brand-name { font-size: 24px; font-weight: 700; color: var(--navy); }

  .intro-panel {
    position: absolute; left: 132px; top: 212px; width: 468px; height: 169px;
    background: var(--panel); padding: 17px 24px 0 24px;
  }
  .intro-handle { font-size: 28px; font-weight: 400; color: var(--coral); line-height: 1.2; letter-spacing: -0.2px; }
  .intro-regions { font-size: 16px; color: var(--ink); margin-top: 7px; }
  .start-button {
    position: absolute; left: 24px; top: 95px; width: 120px; height: 48px;
    background: var(--navy); color: var(--white); border-radius: 2px;
    display: flex; align-items: center; justify-content: center; gap: 10px;
    font-size: 19px; font-weight: 600; text-decoration: none;
  }

  .partner-band {
    position: absolute; left: 0; top: 448px; width: 1200px; height: 96px; background: var(--band);
  }
  .carousel-arrow { position: absolute; top: 35px; }
  .carousel-arrow.prev { left: 40px; }
  .carousel-arrow.next { left: 1144px; }
  .partner-list {
    position: absolute; left: 134px; top: 0; width: 932px; height: 96px;
    display: flex; justify-content: space-between; align-items: center; list-style: none;
  }
  .partner-name { font-size: 19px; font-weight: 700; color: var(--brand-grey); }

  .site-footer { position: absolute; left: 0; top: 544px; width: 1200px; height: 70px; }
  .legal { position: absolute; left: 133px; top: 26px; font-size: 12px; color: var(--ink); }
  .legal a { color: var(--ink); text-decoration: none; }
  .legal .divider { margin: 0 8px; }
  .social-list { position: absolute; left: 847px; top: 21px; display: flex; gap: 7px; list-style: none; }
  .social-link { display: block; width: 26px; height: 26px; border-radius: 50%; }
  .social-1 { background: var(--social-1); }
  .social-2 { background: var(--social-2); }
  .social-3 { background: var(--social-3); }
  .social-4 { background: var(--social-4); }
  .social-5 { background: var(--social-5); }
  .social-6 { background: var(--social-6); }
  .social-7 { background: var(--social-7); }
</style>
</head>
<body>
  <header class="hero">
    <div class="hero-scene" role="img" aria-label="Backpacker with a large rucksack standing on a rock above misty snow-capped mountain ranges under a pale blue sky"></div>

    <div class="brand">
      <span class="brand-dot"></span>
      <span class="brand-name">Trail Buzz Journeys</span>
    </div>

    <section class="intro-panel">
      <h1 class="intro-handle">@RoamQuestOutfitters</h1>
      <p class="intro-regions">Australia | New Zealand | Fiji | South East Asia</p>
      <a class="start-button" href="#destinations">START
        <svg width="15" height="15" viewBox="0 0 16 16" aria-hidden="true">
          <circle cx="8" cy="8" r="8" fill="#ffffff"/>
          <path d="M4 8h6.5M7.5 4.8 10.7 8 7.5 11.2" stroke="#2e3a55" stroke-width="2" fill="none" stroke-linecap="round" stroke-linejoin="round"/>
        </svg>
      </a>
    </section>
  </header>

  <section class="partner-band" aria-label="Our suppliers">
    <svg class="carousel-arrow prev" width="14" height="26" viewBox="0 0 14 26" aria-label="Previous">
      <path d="M12 2 2 13l10 11" stroke="var(--arrow-grey)" stroke-width="2" fill="none"/>
    </svg>
    <ul class="partner-list">
      <li class="partner-name">KESTA</li>
      <li class="partner-name">Harlow Bay</li>
      <li class="partner-name">Vantor</li>
      <li class="partner-name">Orlen Surf</li>
      <li class="partner-name">miragirl</li>
      <li class="partner-name">ZEZE</li>
      <li class="partner-name">ROVEWAY</li>
    </ul>
    <svg class="carousel-arrow next" width="14" height="26" viewBox="0 0 14 26" aria-label="Next">
      <path d="M2 2l10 11L2 24" stroke="var(--arrow-grey)" stroke-width="2" fill="none"/>
    </svg>
  </section>

  <footer class="site-footer">
    <p class="legal">Copyright &nbsp;©&nbsp; 2017&nbsp; Trail Buzz Journeys.&nbsp; <a href="#terms">Terms and Conditions</a><span class="divider">&nbsp;|&nbsp;</span><a href="#contact">Contact Us</a></p>
    <ul class="social-list">
      <li><a class="social-link social-1" href="#" aria-label="Social link 1"></a></li>
      <li><a class="social-link social-2" href="#" aria-label="Social link 2"></a></li>
      <li><a class="social-link social-3" href="#" aria-label="Social link 3"></a></li>
      <li><a class="social-link social-4" href="#" aria-label="Social link 4"></a></li>
      <li><a class="social-link social-5" href="#" aria-label="Social link 5"></a></li>
      <li><a class="social-link social-6" href="#" aria-label="Social link 6"></a></li>
      <li><a class="social-link social-7" href="#" aria-label="Social link 7"></a></li>
    </ul>
  </footer>
</body>
</html>
```